Junior tennis development pathway graphic

The National Racquet Sport Union(NRSU) and the Global Court Games Council (GCGC)
recommend (read demand) that all junior tennis programs now be ran using a progressive format of 4 different colored balls, different court sizes and scoring systems for various ages. We want to create a graphic for our juniors page on our web site that will show parents in a VERY EASY to understand way how their kids will progress through the various stages of tennis. The page is being built using Bootstrap and we plan to use jQuerry Hotspot to give detailed information over certain areas of the graphic. This specific information will be Dbase driven with class names,and specific class info. - The design does not need to show this, I just though it might be helpful to know
Updates

There are 2 other sites that will be helpful in understanding this project:

The first is www.smallplayerscourt.com and the second is my junior page on my current website
www.pinebrookracquetclub.com/juniora.cfm

I added a new file named jr pathway 2

This is an idea i had for the project - needs to be completed and given some sizzle

Target Market(s)

Parents of children ages 3-16

Industry/Entity Type

Progressive

Requirements
Must have
• Vector format
800x800 pixels max
EASY TO UNDERSTAND
Use of some or all of the key words and phrases in the uploaded file "keywords"
Should not have
• I do not want it to look like every other development graphic already out there.
To see what is currently being used image search
"tennis pathway" or "junior tennis pathway"

"pathway and" juniorspathway" in the uploaded files section are 2 ideas of VERY bad attempts

```html
<!DOCTYPE html>
<html lang="en">
<head>
<meta charset="utf-8">
<title>4 Colors One Game – Junior Pathway</title>
<link rel="stylesheet" href="https://fonts.googleapis.com/css2?family=Montserrat:wght@400;600;700&display=swap">
<style>
  :root{
    --red:#ee3439; --red-deep:#5f0c07;
    --orange:#ef7244; --orange-deep:#5f3312;
    --green:#84ad47; --green-deep:#38491f;
    --yellow:#f6ef4c; --yellow-soft:#f1ea7c; --yellow-deep:#6a6333;
    --white:#ffffff;
    --frame:#cfc6b6;
    --title-tint:#dcc9b9;
    --accent:#f04e23;
    --ink:#3b3b3b;
    --ball-lime:#d9ea3f;
  }
  *{margin:0;padding:0;box-sizing:border-box}
  html,body{width:1200px;height:1200px;overflow:hidden;background:#fff}
  body{font-family:"Montserrat",Arial,sans-serif;color:var(--white)}
  .poster{position:relative;width:1200px;height:1200px;overflow:hidden}
  .band{position:absolute;top:0;width:300px;height:1200px}
  .band-red{left:0;background:linear-gradient(var(--red) 0 717px,var(--red-deep) 717px)}
  .band-orange{left:300px;background:linear-gradient(var(--orange) 0 717px,var(--orange-deep) 717px)}
  .band-green{left:600px;background:linear-gradient(var(--green) 0 717px,var(--green-deep) 717px)}
  .band-yellow{left:900px;background:linear-gradient(var(--yellow) 0,var(--yellow-soft) 717px,var(--yellow-deep) 717px)}
  .player{position:absolute;border-radius:48% 48% 40% 40%}
  .player-red{left:80px;top:292px;width:210px;height:310px;background:#d52c24}
  .player-orange{left:335px;top:318px;width:220px;height:372px;background:#de6236}
  .player-green{left:585px;top:372px;width:250px;height:392px;background:#73983b}
  .player-yellow{left:915px;top:482px;width:270px;height:455px;background:#e7c0b3;opacity:.85}
  .hero-number,.hero-line,.tagline,.age,.stage-title,.item{position:absolute;line-height:1;white-space:nowrap}
  .hero-number{left:80px;top:-48px;font-size:390px;font-weight:700;transform:scaleX(.9);transform-origin:left top}
  .hero-line{font-weight:700}
  .hero-colors{left:311px;top:24px;font-size:134px;letter-spacing:-5px}
  .hero-game{left:318px;top:156px;font-size:98px;letter-spacing:-1px}
  .tagline{left:320px;top:270px;font-size:18.8px;font-weight:700}
  .program{position:absolute;left:956px;top:270px}
  .program-title{font-size:19px;font-weight:600;color:var(--accent);line-height:1}
  .program-list{list-style:none;margin-top:11px;font-size:19px;line-height:25px;color:var(--ink)}
  .age{font-size:18.5px;font-weight:700}
  .age-red{left:98px;top:632px}
  .age-orange{left:467px;top:632px}
  .age-green{left:788px;top:650px}
  .age-yellow{left:1043px;top:801px}
  .frames{position:absolute;left:0;top:0}
  .stage-title{font-size:44px;font-weight:700;color:var(--title-tint);transform:translateX(-50%)}
  .title-learn{left:447px;top:744px}
  .title-play{left:447px;top:893px}
  .title-compete{left:718px;top:1026px}
  .item{font-size:24px;font-weight:600}
  .item-two{line-height:32px}
  .item-two-tight{line-height:31px}
</style>
</head>
<body>
<main class="poster">
  <div class="band band-red"></div>
  <div class="band band-orange"></div>
  <div class="band band-green"></div>
  <div class="band band-yellow"></div>

  <div class="player player-red" role="img" aria-label="Illustration of a young child hitting a backhand with a red-stage racquet"></div>
  <div class="player player-orange" role="img" aria-label="Illustration of a girl in a blue outfit preparing a forehand"></div>
  <div class="player player-green" role="img" aria-label="Illustration of a boy in a cap and green shorts hitting a two-handed backhand"></div>
  <div class="player player-yellow" role="img" aria-label="Illustration of a teenage girl in pink following through on a forehand"></div>

  <div class="hero-number">4</div>
  <div class="hero-line hero-colors">COLORS</div>
  <div class="hero-line hero-game">ONE GAME</div>
  <p class="tagline">YOUR CHILD’S PATH TO SUCCESS AT EVERY LEVEL (AGE)</p>

  <div class="program">
    <p class="program-title">What is a program?</p>
    <ul class="program-list">
      <li>-teaching/coaching</li>
      <li>-training/practicing</li>
      <li>-competition</li>
      <li>-play</li>
      <li>-social</li>
    </ul>
  </div>

  <p class="age age-red">Age: 5-8</p>
  <p class="age age-orange">Age: 7-10</p>
  <p class="age age-green">Age: 10-14</p>
  <p class="age age-yellow">Age: 10-18</p>

  <svg class="frames" width="1200" height="1200" viewBox="0 0 1200 1200" aria-hidden="true">
    <defs>
      <symbol id="ball" viewBox="-30 -30 60 60">
        <circle r="27" fill="currentColor"/>
        <path d="M-8,-25.8 C4,-12 4,12 -8,25.8 A27,27 0 0 1 -8,-25.8 Z" fill="var(--ball-lime)"/>
        <path d="M-8,-25.8 C4,-12 4,12 -8,25.8" fill="none" stroke="#fff" stroke-width="3"/>
        <circle r="27" fill="none" stroke="#fff" stroke-width="2"/>
      </symbol>
    </defs>
    <g fill="none" stroke="var(--frame)" stroke-width="3">
      <path d="M370 770 H13 V859 H892 V770 H528"/>
      <path d="M388 918 H13 V1004 H892 V918 H508"/>
      <path d="M596 1058 H311 V1145 H900 L916 1173 H1187 V1025 H938 L900 1058 H838"/>
    </g>
    <use href="#ball" x="73" y="793" width="54" height="54" color="var(--red)"/>
    <use href="#ball" x="350" y="793" width="54" height="54" color="var(--orange)"/>
    <use href="#ball" x="645" y="793" width="54" height="54" color="var(--green)"/>
    <use href="#ball" x="73" y="933" width="54" height="54" color="var(--red)"/>
    <use href="#ball" x="350" y="933" width="54" height="54" color="var(--orange)"/>
    <use href="#ball" x="645" y="933" width="54" height="54" color="var(--green)"/>
    <use href="#ball" x="350" y="1078" width="54" height="54" color="var(--orange)"/>
    <use href="#ball" x="645" y="1078" width="54" height="54" color="var(--green)"/>
    <use href="#ball" x="940" y="1031" width="54" height="54" color="var(--yellow)"/>
    <use href="#ball" x="940" y="1103" width="54" height="54" color="var(--yellow)"/>
  </svg>

  <h2 class="stage-title title-learn">Learn</h2>
  <h2 class="stage-title title-play">Play</h2>
  <h2 class="stage-title title-compete">Compete</h2>

  <p class="item" style="left:145px;top:808px">Red 1</p>
  <p class="item" style="left:421px;top:808px">Orange 1</p>
  <p class="item" style="left:716px;top:808px">Green 1</p>

  <p class="item" style="left:145px;top:948px">Red 2</p>
  <p class="item" style="left:421px;top:948px">Orange 2</p>
  <p class="item item-two" style="left:716px;top:932px">Junior Tennis<br>League</p>

  <p class="item" style="left:421px;top:1093px">JCT Orange</p>
  <p class="item" style="left:716px;top:1093px">JCT Green</p>
  <p class="item" style="left:1015px;top:1046px">JCT Yellow</p>
  <p class="item item-two-tight" style="left:1020px;top:1096px">High school<br>team</p>
</main>
</body>
</html>
```